Harbourline Estate Group

The card is to be black

On the front it will say "Harbourline"
And just under it in smaller writing "Property Group" in dark brown or rose gold

Daniel Forsett
0471 586 209
Admin@harblinegroup.example

On the back it is to say Harbourline Estate group same style as the front but smaller.
And then under that say:
Electrical
General Maintenance
Building works & construction
Energy Consulants

Target Market(s)

Re

Industry/Entity Type

Electrical

Contact Information for Business Card

The card is to be black

Daniel Forsett
0471 586 209
Admin@harblinegroup.example

And then under that say:
Electrical
General Maintenance
Energy Consulants

And somewhere else put residential domestic and industrial

Font styles to use
Serif

Requirements
Should not have
• No pictures of tools etc just a plain sleek card

```html
<!DOCTYPE html>
<html lang="en">
<head>
<meta charset="utf-8">
<title>Harbourline Estate Group – Business Card</title>
<link href="https://fonts.googleapis.com/css2?family=Playfair+Display:wght@600&family=Lora:wght@400;500&display=swap" rel="stylesheet">
<style>
  :root {
    --backdrop: #e4e1de;
    --card-black: #111111;
    --ink-light: #f4f1ee;
    --ink-soft: #c9c4bf;
    --rose-gold: #c99883;
    --rule-rose: rgba(201,152,131,0.7);
  }
  * { margin: 0; padding: 0; box-sizing: border-box; }
  html, body {
    width: 1200px; height: 1000px; overflow: hidden;
    background: var(--backdrop);
  }
  .card {
    position: absolute; left: 220px; width: 761px;
    background: var(--card-black);
    text-align: center;
    box-shadow: 0 6px 18px rgba(0,0,0,0.3);
  }
  .card--front { top: 50px; height: 433px; }
  .card--back { top: 524px; height: 436px; }

  .wordmark__name, .wordmark__sub {
    position: absolute; left: 0; right: 0;
    font-family: "Playfair Display", serif; font-weight: 600; line-height: 1;
  }
  .wordmark__name { color: var(--ink-light); letter-spacing: 2px; }
  .wordmark__sub {
    display: flex; align-items: center; justify-content: center; gap: 14px;
    color: var(--rose-gold); letter-spacing: 1.5px;
  }
  .wordmark__sub::before, .wordmark__sub::after {
    content: ""; height: 1px; background: var(--rule-rose);
  }

  .card--front .wordmark__name { top: 166px; font-size: 60px; }
  .card--front .wordmark__sub { top: 237px; font-size: 26px; }
  .card--front .wordmark__sub::before, .card--front .wordmark__sub::after { width: 90px; }

  .services {
    position: absolute; left: 0; right: 0; top: 339px;
    font-family: "Lora", serif; font-size: 15.5px; line-height: 29px;
    color: var(--ink-soft);
  }

  .card--back .wordmark__name { top: 92px; font-size: 52px; }
  .card--back .wordmark__sub { top: 155px; font-size: 23px; }
  .card--back .wordmark__sub::before, .card--back .wordmark__sub::after { width: 80px; }

  .contact-name {
    position: absolute; left: 0; right: 0; top: 229px; line-height: 1;
    font-family: "Lora", serif; font-weight: 500; font-size: 24px; letter-spacing: 1.5px;
    color: var(--rose-gold);
  }
  .contact-rule {
    position: absolute; left: 285px; width: 190px; top: 270px; height: 1px;
    background: linear-gradient(to right, transparent, var(--rule-rose), transparent);
  }
  .contact-details {
    position: absolute; left: 0; right: 0; top: 284px;
    font-family: "Lora", serif; font-size: 16.5px; line-height: 27px; letter-spacing: 0.3px;
    color: var(--ink-soft); list-style: none;
  }
</style>
</head>
<body>
  <section class="card card--front">
    <div class="wordmark__name">HARBOURLINE</div>
    <div class="wordmark__sub">ESTATE GROUP</div>
    <p class="services">Electrical | General Maintenance | Building works &amp; construction | Energy Consultants<br>Residential domestic and industrial</p>
  </section>

  <section class="card card--back">
    <div class="wordmark__name">HARBOURLINE</div>
    <div class="wordmark__sub">ESTATE GROUP</div>
    <div class="contact-name">DANIEL FORSETT</div>
    <div class="contact-rule"></div>
    <ul class="contact-details">
      <li>0471 586 209</li>
      <li>Admin@harblinegroup.example</li>
      <li>www.harblinegroup.example</li>
    </ul>
  </section>
</body>
</html>
```